Online Cooking App Pitch Deck- (THIS IS NOT A FOOD BUSINESS OR FOOD SERVICE, NO FOOD PICTURES)

Project Goal:
Design a visually compelling pitch deck to be used for securing investment. Looking for the pitch deck to be about the design using shapes, colors, fonts and sizes. Must be creative yet simple and clean.
Color Palette:
https://huebrik.io/ff3800-ffe2db-fefefa-2d3e50-010b13

(We want most screens to use #FEFEFA)

This is the current pitch deck we need simplified and redesigned (USE TEXT IN THE VANDREL LINK TO SHOW IN YOUR DESIGN):

https://files.vandrel.net/slides/d/7QpLmZ2kTr84NwXaVbcY0-hoxjdEuvwKt/view?mode=share&uid=503921846170259384712&fmt=true&sd=true

Project is now guaranteed. Remember use the text in the vandrel link in powerpoint design. Use a little more color not just the logo color. Do not use any pictures of food this is not food related business. We care more about style and design of shapes, text, color fonts.

Target Market(s)

Investors (venture capitalists, angel investors) interested in innovative technology solutions within the food industry.

Font styles to use
Serif
Sans Serif

Requirements
Nice to have
• Simple, abstract background non distracting but complementary.
Should not have
• No pictures

```html
<!DOCTYPE html>
<html lang="en">
<head>
<meta charset="utf-8">
<title>Stove &amp; Sage — Investor Overview Deck</title>
<link href="https://fonts.googleapis.com/css2?family=Montserrat:wght@400;500;600;700;800&display=swap" rel="stylesheet">
<style>
:root{
  --orange:#ff3800;
  --blush:#ffe2db;
  --paper:#fefefa;
  --navy:#2d3e50;
  --ink:#010b13;
  --yellow:#f2a900;
  --grey:#9aa0a6;
}
*{box-sizing:border-box;margin:0;padding:0}
html,body{width:1042px;height:1200px;overflow:hidden;background:#fff}
body{font-family:"Montserrat",Arial,sans-serif;color:var(--ink)}
.deck{position:relative;width:1042px;height:1200px;display:grid;
  grid-template-columns:repeat(3,224.5px);column-gap:64.5px;row-gap:17.9px;
  padding:32px 0 0 120px;align-content:start}
.cell{width:224.5px;height:126.2px;position:relative}
.slide{position:absolute;left:0;top:0;width:386px;height:217px;background:var(--paper);
  transform:scale(.5815);transform-origin:0 0;overflow:hidden;
  box-shadow:0 3px 9px rgba(0,0,0,.22)}
.slide>*{position:absolute}
.kicker{left:14px;top:10px;font-size:5px;font-weight:700}
.brand{right:14px;top:10px;font-size:5px;font-weight:700}
.footer{left:14px;bottom:8px;font-size:3.6px;font-weight:700}
.pageno{right:14px;bottom:8px;font-size:3.4px;font-weight:700;display:flex;align-items:center;gap:2px}
.pageno::before{content:"";width:10px;height:.6px;background:var(--orange)}
.on-dark{color:var(--paper)}
.deco-top{left:272px;top:14px;width:100px;height:96px;border-radius:48px;
  background:radial-gradient(circle at 60% 40%,rgba(255,56,0,.32),rgba(242,169,0,.16) 55%,rgba(254,254,250,0) 75%)}
.deco-bottom{left:2px;top:86px;width:126px;height:118px;border-radius:58px;
  background:radial-gradient(circle at 45% 60%,rgba(242,169,0,.34),rgba(255,56,0,.16) 55%,rgba(254,254,250,0) 75%)}
.sect-title{font-weight:800;font-size:25px;line-height:1.05;text-align:center;color:var(--ink)}
.body{font-size:4.2px;line-height:1.45;color:#3b3b3b}
.label{font-size:7px;font-weight:700}
.h2{font-size:14px;font-weight:800;line-height:1.2}
.hot{color:var(--orange)}
.spoon{background:var(--blush);border-radius:40px}
.comp-name{font-size:9px;font-weight:700;color:var(--orange);text-align:center;width:100px}
.valuation{font-size:4.6px;font-weight:700}
.valuation span{color:var(--orange)}
.check{width:8px;height:8px;border:1px solid var(--orange)}
.feat-title{font-size:4.8px;font-weight:700;color:var(--orange)}
.year{font-size:11px;font-weight:800;color:var(--orange)}
.fin{font-size:3.6px;font-weight:700}
.fin-val{font-size:7px;font-weight:700}
.bubble{border-radius:50%;display:flex;flex-direction:column;justify-content:center;padding:0 10px;font-size:3.4px;line-height:1.3}
.bubble b{font-size:5px}
</style>
</head>
<body>
<main class="deck">

  <!-- 1 Cover -->
  <div class="cell"><section class="slide">
    <div class="deco-top" role="img" aria-label="Abstract ring and circle motif in orange, yellow and navy" style="left:290px;top:6px;width:90px;height:70px"></div>
    <div class="deco-bottom" role="img" aria-label="Abstract ring and circle motif in grey, yellow and orange" style="top:90px"></div>
    <div style="left:0;width:386px;top:62px;text-align:center;font-size:24px;font-weight:700">Stove &amp; Sage</div>
    <div style="left:0;width:386px;top:96px;text-align:center;font-size:15px;font-weight:800">INVESTOR OVERVIEW</div>
    <div style="left:0;width:386px;top:124px;text-align:center;font-size:9px;line-height:1.5;color:#555">THIS DOCUMENT EXISTS FOR<br>OUR FUTURE PARTNERS.</div>
    <div class="footer" style="left:158px">Proprietary and Confidential</div>
  </section></div>

  <!-- 2 What is -->
  <div class="cell"><section class="slide">
    <div class="kicker">Cook Learn Repeat</div><div class="brand">Stove &amp; Sage</div>
    <div class="h2" style="left:14px;top:55px;font-size:13px"><span class="hot">What Is</span> Stove <span class="hot">&amp;</span> Sage?</div>
    <p class="body" style="left:14px;top:82px;width:290px">Stove &amp; Sage is an online cooking platform that connects home cooks with chefs through live, interactive classes. Learners pick a cuisine, join a small group session and cook along in real time while the chef guides each step, answers questions and shares kitchen techniques. Classes range from quick weeknight meals to regional specialties, with recordings, shopping lists and prep notes sent before every session so nobody starts unprepared.</p>
    <p class="body" style="left:14px;top:136px;width:290px">Chefs set their own schedules, prices and menus, while the platform handles bookings, payments and streaming. The result is a flexible, social way to learn cooking from anywhere, built for busy people who want real skills.</p>
    <div class="footer">Proprietary and Confidential</div><div class="pageno">3</div>
  </section></div>

  <!-- 3 Consumer insights -->
  <div class="cell"><section class="slide">
    <div class="kicker">Cook Learn Repeat</div><div class="brand">Stove &amp; Sage</div>
    <div class="deco-top" role="img" aria-label="Abstract ring and circle motif in orange, yellow and navy"></div>
    <div class="deco-bottom" role="img" aria-label="Abstract ring and circle motif in grey, yellow and orange"></div>
    <div class="sect-title" style="left:80px;width:250px;top:40px">Consumer<br>Insights</div>
    <div class="footer">Proprietary and Confidential</div><div class="pageno">4</div>
  </section></div>

  <!-- 4 Insight 1 -->
  <div class="cell"><section class="slide">
    <div class="kicker">Cook Learn Repeat</div><div class="brand">Stove &amp; Sage</div>
    <div class="label" style="left:14px;top:32px;font-size:5.5px">Insight 1</div>
    <div class="h2" style="left:14px;top:44px;font-size:11px">Growing Interest In<br><span class="hot">Virtual Cooking Classes</span></div>
    <p class="body" style="left:14px;top:76px;width:300px">Consumers seeking alternatives, more choices, easier preference management, or simply a way to avoid crowded spaces are increasingly turning to online culinary education platforms. This trend is fueled by the desire to learn new cooking skills, explore different cuisines, and enjoy cooking as a leisure activity or a bonding experience with friends and family.</p>
    <div class="footer">Proprietary and Confidential</div><div class="pageno">5</div>
  </section></div>

  <!-- 5 Insight 2 -->
  <div class="cell"><section class="slide">
    <div class="kicker">Cook Learn Repeat</div><div class="brand">Stove &amp; Sage</div>
    <div class="spoon" role="img" aria-label="Abstract ladle shape in soft pink" style="left:26px;top:36px;width:50px;height:150px;border-radius:10px 10px 30px 30px"></div>
    <div class="label" style="right:14px;top:32px;font-size:5.5px">Insight 2</div>
    <div class="h2" style="right:14px;top:44px;font-size:11px;text-align:right">Demand For Interactive And<br><span class="hot">Personalized Experience</span></div>
    <p class="body" style="right:14px;top:76px;width:240px;text-align:right">Consumers value interactive and personalized virtual cooking experiences. This includes live classes with real-time feedback from chefs, personalized meal planning, and customization options that cater to dietary restrictions or preferences. Platforms that offer these personal interactions tend to be more popular.</p>
    <div class="footer">Proprietary and Confidential</div><div class="pageno">6</div>
  </section></div>

  <!-- 6 Insight 3 -->
  <div class="cell"><section class="slide">
    <div class="kicker">Cook Learn Repeat</div><div class="brand">Stove &amp; Sage</div>
    <div class="spoon" role="img" aria-label="Abstract spoon shape in soft pink" style="left:30px;top:60px;width:22px;height:100px;transform:rotate(-45deg)"></div>
    <div class="label" style="right:14px;top:32px;font-size:5.5px">Insight 3</div>
    <div class="h2" style="right:14px;top:44px;font-size:11px;text-align:right">Global Cuisine<br><span class="hot">Exploration</span></div>
    <p class="body" style="right:14px;top:76px;width:240px;text-align:right">There is a marked interest in exploring global cuisines through virtual cooking classes. Consumers are eager to learn about and experiment with dishes from different cultures, driven by a desire for new experiences and flavors. This trend is made easier by the accessibility of virtual classes, which connect chefs and learners around the world.</p>
    <div class="footer">Proprietary and Confidential</div><div class="pageno">7</div>
  </section></div>

  <!-- 7 The problem section -->
  <div class="cell"><section class="slide">
    <div class="kicker">Cook Learn Repeat</div><div class="brand">Stove &amp; Sage</div>
    <div class="deco-top" role="img" aria-label="Abstract ring and circle motif in orange, yellow and navy"></div>
    <div class="deco-bottom" role="img" aria-label="Abstract ring and circle motif in grey, yellow and orange"></div>
    <div class="sect-title" style="left:80px;width:220px;top:56px;font-size:24px">The Problem</div>
    <div class="footer">Proprietary and Confidential</div><div class="pageno">8</div>
  </section></div>

  <!-- 8 The problem -->
  <div class="cell"><section class="slide">
    <div class="kicker">Cook Learn Repeat</div><div class="brand">Stove &amp; Sage</div>
    <div class="h2" style="left:14px;top:45px;font-size:11px">The<br><span class="hot">Problem</span></div>
    <p class="body" style="left:14px;top:78px;width:290px">Learning to cook well is harder than it should be. In-person classes are expensive, booked out weeks ahead and limited to a few cities. Recorded videos are cheap but one-way: nobody tastes your sauce, corrects your knife grip or explains why the dough failed. Home cooks with allergies or dietary preferences rarely find lessons that fit them, and talented chefs without a restaurant stage struggle to reach students, set prices or build a steady teaching income.</p>
    <div class="footer">Proprietary and Confidential</div><div class="pageno">9</div>
  </section></div>

  <!-- 9 Market opportunity -->
  <div class="cell"><section class="slide">
    <div class="kicker">Cook Learn Repeat</div><div class="brand">Stove &amp; Sage</div>
    <div class="deco-top" role="img" aria-label="Abstract ring and circle motif in orange, yellow and navy"></div>
    <div class="deco-bottom" role="img" aria-label="Abstract ring and circle motif in grey, yellow and orange"></div>
    <div class="sect-title" style="left:95px;width:240px;top:44px">Market<br>Opportunity</div>
    <div class="footer">Proprietary and Confidential</div><div class="pageno">10</div>
  </section></div>

  <!-- 10 Insight healthier -->
  <div class="cell"><section class="slide">
    <div class="kicker">Cook Learn Repeat</div><div class="brand">Stove &amp; Sage</div>
    <div class="label" style="left:14px;top:32px;font-size:5.5px">Insight 1</div>
    <div class="h2" style="left:14px;top:44px;font-size:11px">Increasing Demand For<br><span class="hot">Healthier Home-cooked Meals</span></div>
    <p class="body" style="left:14px;top:76px;width:290px">More households want to know exactly what goes into their food. Rising interest in balanced diets, portion control and fresh ingredients is pushing people back into their own kitchens, yet many lack the confidence to cook nourishing meals without guidance. Live classes that teach practical, healthy techniques meet this need directly and build habits that last well beyond a single lesson.</p>
    <div class="footer">Proprietary and Confidential</div><div class="pageno">11</div>
  </section></div>

  <!-- 11 Insight convenience -->
  <div class="cell"><section class="slide">
    <div class="kicker">Cook Learn Repeat</div><div class="brand">Stove &amp; Sage</div>
    <div class="label" style="left:14px;top:32px;font-size:5.5px">Insight 2</div>
    <div class="h2" style="left:14px;top:43px;font-size:11px">Convenience And<br><span class="hot">Time-saving Solutions</span></div>
    <p class="body" style="left:14px;top:74px;width:220px">Another key insight is the high demand for convenience and time-saving solutions, particularly among busy households and individuals with fast-paced lifestyles. Short classes and prep guides fit right into a full week.</p>
    <div class="footer">Proprietary and Confidential</div><div class="pageno">12</div>
  </section></div>

  <!-- 12 Current solutions -->
  <div class="cell"><section class="slide">
    <div class="kicker">Cook Learn Repeat</div><div class="brand">Stove &amp; Sage</div>
    <div class="deco-top" role="img" aria-label="Abstract ring and circle motif in orange, yellow and navy"></div>
    <div class="deco-bottom" role="img" aria-label="Abstract ring and circle motif in grey, yellow and orange"></div>
    <div class="sect-title" style="left:85px;width:240px;top:44px">Current<br>Solutions</div>
    <div class="footer">Proprietary and Confidential</div><div class="pageno">13</div>
  </section></div>

  <!-- 13 Competitors -->
  <div class="cell"><section class="slide">
    <div class="kicker">Cook Learn Repeat</div><div class="brand">Stove &amp; Sage</div>
    <div class="label" style="left:16px;top:22px">Competitors</div>
    <div class="comp-name" style="left:40px;top:38px;color:var(--ink)">StageChef</div>
    <div class="comp-name" style="left:142px;top:38px;color:var(--navy)">Table Rue</div>
    <div class="comp-name" style="left:246px;top:38px">Cookhaven</div>
    <p class="body" style="left:40px;top:56px;width:92px;font-size:3.6px">StageChef, a leader in online prerecorded learning, offers celebrity-taught video courses across many subjects. Their high production value and renowned instructors make them a powerhouse in the premium learning space.</p>
    <p class="body" style="left:142px;top:56px;width:92px;font-size:3.6px">Table Rue was a prominent player in the high-end kitchenware and cooking class space. They offered in-store shopping experiences with premium cookware and ingredients, alongside engaging cooking classes led by culinary professionals.</p>
    <p class="body" style="left:246px;top:56px;width:92px;font-size:3.6px">Cookhaven, another player in the online culinary education space, provides in-person and online cooking classes with a focus on connecting users with local chefs. They offer a variety of class formats, from group courses to private chef experiences.</p>
    <div class="valuation" style="left:50px;top:132px">Estimated Valuation: <span>$2.7B</span></div>
    <div class="valuation" style="left:152px;top:132px">Estimated Valuation: <span>$50M</span></div>
    <div class="valuation" style="left:256px;top:132px">Estimated Valuation: <span>$2.4M</span></div>
    <p class="body" style="left:24px;top:148px;width:340px;font-size:3.8px;text-align:center"><b>Key Takeaway:</b> Each competitor covers one piece of the experience, either polished video, premium retail or local bookings. None combines live interaction, global chefs and flexible pricing in one place, which leaves room for a platform built around real-time teaching and chef independence.</p>
    <div class="footer">Proprietary and Confidential</div><div class="pageno">14</div>
  </section></div>

  <!-- 14 Better solution -->
  <div class="cell"><section class="slide">
    <div class="kicker">Cook Learn Repeat</div><div class="brand">Stove &amp; Sage</div>
    <div class="deco-top" role="img" aria-label="Abstract ring and circle motif in orange, yellow and navy"></div>
    <div class="deco-bottom" role="img" aria-label="Abstract ring and circle motif in grey, yellow and orange"></div>
    <div class="sect-title" style="left:120px;top:44px;text-align:left">A Better<br>Solution</div>
    <div class="footer">Proprietary and Confidential</div><div class="pageno">15</div>
  </section></div>

  <!-- 15 Quote -->
  <div class="cell"><section class="slide">
    <div class="kicker">Cook Learn Repeat</div><div class="brand">Stove &amp; Sage</div>
    <blockquote style="left:0;width:386px;top:42px;text-align:center;font-size:11px;font-weight:700;line-height:1.35">“Cooking will never be good if it<br>isn’t made with love for the person<br>it’s being made for.”</blockquote>
    <div style="right:16px;top:92px;font-size:8px;color:#444">- Henri Marlot</div>
    <div class="footer">Proprietary and Confidential</div><div class="pageno">16</div>
  </section></div>

  <!-- 16 Why we're different -->
  <div class="cell"><section class="slide">
    <div style="left:0;top:0;width:107px;height:217px;background:var(--navy)"></div>
    <div class="kicker on-dark">Cook, Learn, Repeat</div>
    <div class="on-dark" style="left:14px;top:24px;font-size:9.5px;font-weight:800;line-height:1.2">Why we’re<br>different</div>
    <div class="on-dark" style="left:14px;top:72px;width:84px;font-size:4.6px;font-weight:700;line-height:1.4">Forget Gatekeepers, Unleash Passion: Stove &amp; Sage Revolutionizes Culinary Education</div>
    <p class="body" style="left:14px;top:104px;width:84px;color:#d7dce2;font-size:3.8px">The current culinary education landscape is dominated by limited options. Learners choose between costly studios and passive videos, while chefs wait for someone else to give them a stage.</p>
    <div class="footer on-dark">Proprietary and Confidential</div>
    <div class="brand">Stove &amp; Sage</div>
    <div class="check" style="left:120px;top:22px"></div>
    <div class="feat-title" style="left:134px;top:22px">Anyone Can Host</div>
    <p class="body" style="left:134px;top:29px;width:236px;font-size:3.4px">Every qualified cook can open a virtual kitchen, set a schedule and start teaching. No storefront, no studio lease and no waiting list, just a camera, a stove and a recipe worth sharing with the world.</p>
    <div class="check" style="left:120px;top:62px"></div>
    <div class="feat-title" style="left:134px;top:62px">Unleash the Global Kitchen: Real-Time Learning Without Borders</div>
    <p class="body" style="left:134px;top:69px;width:236px;font-size:3.4px">Forget pre-recorded lessons and geographic limits. Live classes foster a dynamic learning space where questions get answered instantly, techniques are corrected on the spot and cooks connect across time zones. Imagine learning a street snack from its home city or a classic bread from a village baker, all from your own kitchen.</p>
    <div class="check" style="left:120px;top:118px"></div>
    <div class="feat-title" style="left:134px;top:118px">Empowering Chefs, Building Sustainable Income</div>
    <p class="body" style="left:134px;top:125px;width:236px;font-size:3.4px">Chefs gain tools to build a thriving online business. <b>Monetize Your Expertise:</b> set prices for classes, consultations and workshops. <b>Leverage Existing Audiences:</b> invite followers straight into paid sessions. <b>Flexible Income Streams:</b> mix group classes, private lessons and recipe bundles to keep earnings steady across every season.</p>
    <div class="pageno">17</div>
  </section></div>

  <!-- 17 Demo -->
  <div class="cell"><section class="slide" style="background:var(--navy)">
    <div class="kicker on-dark" style="opacity:.5">Cook Learn Repeat</div>
    <div class="brand on-dark" style="opacity:.5">Stove &amp; Sage</div>
    <div class="on-dark" style="left:14px;top:80px;font-size:13px;font-weight:800;line-height:1.2">Our<br><span class="hot">Demo</span></div>
    <div style="left:94px;top:24px;width:279px;height:163px;background:var(--paper);border:1.5px solid var(--blush)"></div>
    <svg style="left:226px;top:100px" width="12" height="10" viewBox="0 0 12 10" aria-label="Play video"><rect x=".5" y=".5" width="11" height="9" fill="none" stroke="#999" stroke-width=".7"/><path d="M5 3 L8 5 L5 7Z" fill="#999"/></svg>
    <div class="footer on-dark" style="opacity:.5">Proprietary and Confidential</div><div class="pageno on-dark" style="opacity:.5">18</div>
  </section></div>

  <!-- 18 Timeline -->
  <div class="cell"><section class="slide">
    <div class="kicker">Cook Learn Repeat</div><div class="brand">Stove &amp; Sage</div>
    <div class="label" style="left:12px;top:22px;font-size:9.5px">Project Timeline - 2024</div>
    <div class="feat-title" style="left:16px;top:40px;font-size:3.2px">Ideation &amp; Design</div>
    <p class="body" style="left:16px;top:45px;width:90px;font-size:2.8px">• Brainstorm and define project concept<br>• User research and target audience mapping<br>• Develop project requirements and specs<br>• Create initial design mockups</p>
    <div class="feat-title" style="left:192px;top:40px;font-size:3.2px">Development &amp; Pre-Marketing</div>
    <p class="body" style="left:192px;top:45px;width:110px;font-size:2.8px">• Source first-round funding<br>• Front-end and back-end development<br>• Integrate functionality based on design<br>• Testing and quality fixes<br>• Prepare marketing materials, website and social content<br>• Identify target marketing channels<br>• Develop pre-launch marketing strategy</p>
    <div style="left:14px;top:122px;width:90px;height:3px;background:var(--blush)"></div>
    <div style="left:104px;top:122px;width:90px;height:3px;background:#f8c8bb"></div>
    <div style="left:194px;top:122px;width:92px;height:3px;background:var(--navy)"></div>
    <div style="left:286px;top:122px;width:86px;height:3px;background:var(--yellow)"></div>
    <div class="feat-title" style="left:115px;top:112px;font-size:3.4px;color:var(--navy)">Q2 (Complete)</div>
    <div class="feat-title" style="left:304px;top:112px;font-size:3.4px;color:var(--yellow)">Q4 (Upcoming)</div>
    <div class="feat-title" style="left:16px;top:132px;font-size:3.4px">Q1 (Complete)</div>
    <div class="feat-title" style="left:208px;top:132px;font-size:3.4px;color:var(--orange)">Q3 (Current)</div>
    <div class="feat-title" style="left:106px;top:144px;font-size:3px;color:var(--navy)">Design Refinement &amp; Prototyping</div>
    <p class="body" style="left:106px;top:149px;width:80px;font-size:2.6px">• Create high-fidelity mockups and prototypes<br>• Refine and finalize user interface<br>• Develop a style guide for consistent branding</p>
    <div class="feat-title" style="left:288px;top:144px;font-size:3px">Launch &amp; Post-Launch Activities</div>
    <p class="body" style="left:288px;top:149px;width:84px;font-size:2.6px">• Final product testing and quality checks<br>• Product launch and early momentum<br>• Initial marketing campaign rollout<br>• User acquisition and onboarding<br>• Gather user feedback and iterate</p>
    <div class="footer">Proprietary and Confidential</div><div class="pageno">19</div>
  </section></div>

  <!-- 19 The team section -->
  <div class="cell"><section class="slide">
    <div class="kicker">Cook Learn Repeat</div><div class="brand">Stove &amp; Sage</div>
    <div class="deco-top" role="img" aria-label="Abstract ring and circle motif in orange, yellow and navy"></div>
    <div class="deco-bottom" role="img" aria-label="Abstract ring and circle motif in grey, yellow and orange"></div>
    <div class="sect-title" style="left:90px;width:210px;top:56px">The Team</div>
    <div class="footer">Proprietary and Confidential</div><div class="pageno">20</div>
  </section></div>

  <!-- 20 Team member -->
  <div class="cell"><section class="slide">
    <div class="kicker">Cook Learn Repeat</div><div class="brand">Stove &amp; Sage</div>
    <div class="label" style="left:14px;top:34px;font-size:5.5px">The Team</div>
    <div style="left:14px;top:46px;font-size:11px;font-weight:800">MAREN ASHBY</div>
    <div style="left:14px;top:60px;font-size:8px;color:var(--orange)">Founder &amp; CEO</div>
    <p class="body" style="left:14px;top:76px;width:200px">Maren founded Stove &amp; Sage after a decade spent in professional kitchens and culinary schools. She has taught thousands of students, launched two online learning ventures and built partnerships with chefs across four continents. Her mission is to give every cook a stage and every learner a seat at the counter, wherever they live.</p>
    <div role="img" aria-label="Portrait photo of the founder" style="left:232px;top:30px;width:76px;height:76px;border-radius:50%;background:radial-gradient(circle at 45% 40%,#c9a58a,#7a6a5c 70%,#5a4e45)"></div>
    <div class="footer">Proprietary and Confidential</div><div class="pageno">21</div>
  </section></div>

  <!-- 21 Revenue model -->
  <div class="cell"><section class="slide">
    <div class="kicker">Cook Learn Repeat</div><div class="brand">Stove &amp; Sage</div>
    <div class="deco-top" role="img" aria-label="Abstract ring and circle motif in orange, yellow and navy"></div>
    <div class="deco-bottom" role="img" aria-label="Abstract ring and circle motif in grey, yellow and orange"></div>
    <div class="sect-title" style="left:95px;width:200px;top:44px">Revenue<br>Model</div>
    <div class="footer">Proprietary and Confidential</div><div class="pageno">22</div>
  </section></div>

  <!-- 22 How we monetize -->
  <div class="cell"><section class="slide">
    <div style="left:0;top:0;width:94px;height:217px;background:var(--yellow)"></div>
    <div class="kicker on-dark">Cook, Learn, Repeat</div>
    <div class="on-dark" style="left:14px;top:34px;font-size:10px;font-weight:800;line-height:1.2">How we<br>monetize.</div>
    <div class="footer on-dark">Proprietary and Confidential</div>
    <div class="brand">Stove &amp; Sage</div>
    <div style="left:108px;top:22px;font-size:8.5px;font-weight:800">Strategy 1.</div>
    <p class="body" style="left:108px;top:35px;width:192px;font-size:3.6px">Commission on every class. Chefs set their own prices and the platform keeps a share of each booking, covering payments, streaming and discovery. As chefs grow their audiences, revenue grows with them, and group sessions let one lesson earn from many seats at once. Premium placement and featured listings offer chefs extra visibility for a small monthly fee.</p>
    <div style="left:108px;top:102px;font-size:8.5px;font-weight:800;color:var(--orange)">Strategy 2.</div>
    <p class="body" style="left:108px;top:115px;width:192px;font-size:3.6px">Learner memberships. A monthly plan unlocks discounted live classes, a library of recorded sessions, meal plans and shopping lists. Members return week after week, creating steady recurring revenue, while gift cards and private events for teams and families add seasonal income on top of the core subscription.</p>
    <div class="pageno">23</div>
  </section></div>

  <!-- 23 Financial projections -->
  <div class="cell"><section class="slide">
    <div class="kicker">Cook Learn Repeat</div><div class="brand">Stove &amp; Sage</div>
    <div class="label" style="left:14px;top:22px;font-size:7px">Financial Projections.</div>
    <div style="left:100px;top:46px;width:.5px;height:80px;background:#ccc"></div>
    <div style="left:192px;top:46px;width:.5px;height:80px;background:#ccc"></div>
    <div style="left:284px;top:46px;width:.5px;height:80px;background:#ccc"></div>

    <div class="year" style="left:14px;top:52px">2024</div>
    <div class="fin" style="left:16px;top:68px">User Growth</div><div class="fin-val" style="left:16px;top:78px">2,000</div>
    <div class="fin" style="left:16px;top:92px">Marketing &amp; Ad’s</div><div class="fin-val" style="left:16px;top:100px">$30,000.00</div>
    <div class="fin" style="left:16px;top:114px">Revenue</div><div class="fin-val" style="left:16px;top:122px">$X00,000.00</div>

    <div class="year" style="left:106px;top:52px">2025</div>
    <div class="fin" style="left:108px;top:68px">User Growth</div><div class="fin-val" style="left:108px;top:78px">12,000</div>
    <div class="fin" style="left:108px;top:92px">Marketing &amp; Ad’s</div><div class="fin-val" style="left:108px;top:100px">$120,000.00</div>
    <div class="fin" style="left:108px;top:114px">Revenue</div><div class="fin-val" style="left:108px;top:122px">$2,X00,000.00</div>

    <div class="year" style="left:198px;top:52px">2026</div>
    <div class="fin" style="left:200px;top:68px">User Growth</div><div class="fin-val" style="left:200px;top:78px">22,000</div>
    <div class="fin" style="left:200px;top:92px">Marketing &amp; Ad’s</div><div class="fin-val" style="left:200px;top:100px">$120,000.00</div>
    <div class="fin" style="left:200px;top:114px">Revenue</div><div class="fin-val" style="left:200px;top:122px">$10,000,000.00</div>

    <div class="year" style="left:290px;top:52px">2027</div>
    <div class="fin" style="left:292px;top:68px">User Growth</div><div class="fin-val" style="left:292px;top:78px">30,000</div>
    <div class="fin" style="left:292px;top:92px">Marketing &amp; Ad’s</div><div class="fin-val" style="left:292px;top:100px">$150,000.00</div>
    <div class="fin" style="left:292px;top:114px">Revenue</div><div class="fin-val" style="left:292px;top:122px">$25,000,000.00</div>
    <div class="footer">Proprietary and Confidential</div><div class="pageno">24</div>
  </section></div>

  <!-- 24 The ask -->
  <div class="cell"><section class="slide">
    <div style="left:0;top:0;width:94px;height:217px;background:var(--orange)"></div>
    <div class="kicker on-dark">Cook, Learn, Repeat</div>
    <div class="on-dark" style="left:12px;top:22px;font-size:11px;font-weight:800">The Ask.</div>
    <p class="body" style="left:12px;top:40px;width:74px;color:var(--blush);font-size:3.8px">We are raising $1M to fund a two-year runway. The capital will complete product development, launch marketing in our first regions and cover daily operations while we grow the chef network and reach our first thirty thousand learners. This round positions Stove &amp; Sage to become the leading live cooking school online, with a clear path to recurring revenue and profitability.</p>
    <div class="footer on-dark">Proprietary and Confidential</div>
    <div class="brand">Stove &amp; Sage</div>
    <div style="left:165px;top:20px;width:180px;height:180px;border:.6px solid #555;border-radius:50%"></div>
    <div class="bubble" style="left:150px;top:0;width:90px;height:90px;background:var(--blush)"><b>Development:</b>Adding new features, ongoing maintenance, front-end design adjustments and implementation.</div>
    <div class="bubble on-dark" style="left:100px;top:63px;width:104px;height:104px;background:var(--orange);align-items:center"><b style="font-size:7.5px;text-align:center;line-height:1.3">Fund<br>allocation</b></div>
    <div class="bubble on-dark" style="left:215px;top:69px;width:80px;height:80px;background:var(--yellow)"><b>Marketing &amp; Advertising:</b>Adding new features, ongoing maintenance and design adjustments.</div>
    <div class="bubble on-dark" style="left:170px;top:122px;width:84px;height:84px;background:var(--navy)"><b>Operations:</b>The day-to-day activities with the team and ongoing management of new relationships.</div>
    <div class="bubble on-dark" style="left:318px;top:87px;width:44px;height:44px;background:var(--ink);align-items:center;text-align:center;padding:0;font-size:4px"><b style="font-size:4.6px">Total<br>2-yr</b>runway<br><b style="font-size:4.6px">$1 M</b></div>
    <div class="bubble" style="left:236px;top:6px;width:20px;height:20px;background:var(--blush);border:.5px solid var(--paper);padding:0;align-items:center;text-align:center;font-size:2.6px"><b style="font-size:2.8px">2-yr</b>$480K</div>
    <div class="bubble on-dark" style="left:276px;top:86px;width:20px;height:20px;background:var(--yellow);padding:0;align-items:center;text-align:center;font-size:2.6px"><b style="font-size:2.8px">2-yr</b>$360K</div>
    <div class="bubble on-dark" style="left:238px;top:186px;width:20px;height:20px;background:var(--navy);padding:0;align-items:center;text-align:center;font-size:2.6px"><b style="font-size:2.8px">2-yr</b>$160K</div>
    <div class="pageno">25</div>
  </section></div>

</main>
</body>
</html>
```